Introduction flyer

Bright Orchard Nutrition & Wellness Consulting, is a new holistic nutritional therapy specialising in womens health. I want a flyer that appeals to women between 15 to 60. It must speak "health, food & balance". I have attached the basic info I need included in the text. I like Greens & Blues, soft text. My flyer will be distributed to cafes, shops, fitness centres, hung up in grocery stores & health centres etc. The QEVR & WRUK logos need to appear on the flyer to show I am fully registered. My own logo & company name is attached.

Target Market(s)

Women from 10 to 60 years old.

Industry/Entity Type

Nutritionist

Colors
32a6d7
abd037
33b8a4
fbf289
ffcf3e
b768aa
d5d5d5
dcdcdc
e8e8e8

Requirements
Must have
• An image of healthy food & ladies. A group of women eating soup, stews or curry type dishes, with plenty of colour - no bread or white wine, and not just fruit please. Food that looks enjoyable to the average person.
• Nutrition is main part of my job, so please keep that in mind & emphasise food & natural well being.
Should not have
• People exercising, men, white wine, bread, cakes, sweets etc..

```html
<!DOCTYPE html>
<html lang="en">
<head>
<meta charset="utf-8">
<title>Bright Orchard Nutrition &amp; Wellness Consulting – Introduction Flyer</title>
<link href="https://fonts.googleapis.com/css2?family=Open+Sans:wght@400;600;700;800&family=Cinzel:wght@700&display=swap" rel="stylesheet">
<style>
  :root{
    --teal:#33b8a4;
    --blue:#32a6d7;
    --green:#abd037;
    --yellow:#fbf289;
    --gold:#ffcf3e;
    --purple:#b768aa;
    --rose:#d93b63;
    --ink:#4a4f55;
    --paper:#ffffff;
  }
  *{margin:0;padding:0;box-sizing:border-box}
  html,body{width:837px;height:1200px;overflow:hidden}
  body{font-family:"Open Sans",Arial,sans-serif;color:var(--ink);background:var(--paper)}
  .flyer{position:relative;width:837px;height:1200px;overflow:hidden;background:var(--paper)}

  .hero-photo{position:absolute;left:0;top:0;width:837px;height:455px;
    background:linear-gradient(120deg,#dfe6e2 0%,#f2efe6 35%,#c9a27a 62%,#e7b24a 78%,#8a8f7a 100%)}

  .home-visit{position:absolute;left:22px;top:128px;width:230px;height:230px;border-radius:50%;
    background:rgba(171,208,55,.88);display:flex;align-items:center;justify-content:center;
    text-align:center;color:#fff;font-size:16px;line-height:1.35;font-weight:600;padding:30px}

  .question-band{position:absolute;left:0;top:455px;width:837px;height:78px;background:var(--teal);
    display:flex;align-items:center;justify-content:center;text-align:center;
    color:#fff;font-weight:800;font-size:21px;line-height:1.3;padding:0 60px;text-transform:uppercase}

  .brand{position:absolute;left:30px;top:560px;display:flex;align-items:center;gap:14px}
  .brand-dot{width:70px;height:70px;border-radius:50%;background:var(--purple)}
  .brand-name{font-family:"Cinzel",serif;font-weight:700;color:var(--purple);font-size:19px;line-height:1.2;width:240px}

  .deco{position:absolute;border-radius:50%}
  .deco-green-big{left:-95px;top:648px;width:450px;height:450px;background:var(--green)}
  .deco-yellow{left:-40px;top:1035px;width:170px;height:170px;background:var(--yellow)}
  .deco-teal{left:100px;top:1080px;width:150px;height:150px;background:var(--teal)}
  .deco-blue{left:230px;top:1140px;width:90px;height:90px;background:var(--blue);opacity:.85}
  .deco-gold{left:335px;top:935px;width:40px;height:40px;background:var(--gold)}

  .diet-message{position:absolute;left:32px;top:740px;width:255px;color:#fff;font-size:12.5px;line-height:1.45}
  .diet-message h2{font-size:14.5px;font-weight:800;line-height:1.3;margin-bottom:12px;text-transform:uppercase}
  .diet-message p{margin-bottom:10px}

  .specialisms{position:absolute;left:430px;top:565px;width:380px}
  .specialisms .intro{color:var(--teal);font-weight:700;font-size:15px;line-height:1.4;text-align:center;margin-bottom:18px}
  .spec-list{list-style:none;width:215px}
  .spec-list li{position:relative;padding-left:26px;font-size:11.5px;line-height:1.35;margin-bottom:9px}
  .spec-list li svg{position:absolute;left:0;top:0;width:17px;height:17px}

  .food-heart{position:absolute;left:655px;top:740px;width:160px;height:150px;border-radius:50% 50% 46% 46%;
    background:radial-gradient(circle at 35% 40%,#e85a3a 0%,#f2a23a 35%,#7cb342 70%,#3f8f3a 100%)}

  .contact{position:absolute;left:420px;top:945px;width:395px;text-align:center;color:var(--rose)}
  .contact .call{font-weight:800;font-size:18px;line-height:1.35}
  .contact .book{font-weight:700;font-size:14.5px;line-height:1.4;margin-top:6px}
  .contact .clinic{font-size:10.5px;line-height:1.4;margin-top:12px;color:var(--rose)}
</style>
</head>
<body>
<main class="flyer">
  <div class="hero-photo" role="img" aria-label="Photograph of a smiling woman enjoying a bowl of colourful vegetable soup in a bright kitchen"></div>

  <div class="home-visit">Home visits available at no extra cost within local area. I can visit your place of work or home.</div>

  <div class="question-band">Do you experience low energy, low libido, menstrual cycle complications, or are you planning a baby?</div>

  <div class="deco deco-green-big"></div>
  <div class="deco deco-yellow"></div>
  <div class="deco deco-teal"></div>
  <div class="deco deco-blue"></div>
  <div class="deco deco-gold"></div>

  <div class="brand">
    <div class="brand-dot"></div>
    <div class="brand-name">Bright Orchard Nutrition &amp; Wellness Consulting</div>
  </div>

  <section class="diet-message">
    <h2>Small changes to your diet may lead to big changes in your health.</h2>
    <p>Eat well, live well.<br>Discover exactly what YOU need to change and how to make these changes long lasting.</p>
    <p>There is no 'one fits all'. My nutritional advice aims to dig up the root cause to my client's health concerns. My lifestyle plans are completely personalised to an individual's needs and circumstances. I consider the whole person not just symptoms or disease.</p>
  </section>

  <section class="specialisms">
    <p class="intro">QEVR &amp; WRUK Registered and fully insured Nutritional Therapist &amp; Wellness Consultant, specialising in:</p>
    <ul class="spec-list">
      <li><svg viewBox="0 0 20 20"><circle cx="10" cy="10" r="9" fill="none" stroke="#33b8a4" stroke-width="1.6"/><path d="M5.5 10.5l3 3 6-6.5" fill="none" stroke="#abd037" stroke-width="2"/></svg>Fertility, IVF, pre-conception, pregnancy &amp; post-natal care</li>
      <li><svg viewBox="0 0 20 20"><circle cx="10" cy="10" r="9" fill="none" stroke="#33b8a4" stroke-width="1.6"/><path d="M5.5 10.5l3 3 6-6.5" fill="none" stroke="#abd037" stroke-width="2"/></svg>Menstrual cycle challenges (PCOS, Endometriosis, PMS, heavy/irregular periods etc)</li>
      <li><svg viewBox="0 0 20 20"><circle cx="10" cy="10" r="9" fill="none" stroke="#33b8a4" stroke-width="1.6"/><path d="M5.5 10.5l3 3 6-6.5" fill="none" stroke="#abd037" stroke-width="2"/></svg>Thyroid conditions</li>
      <li><svg viewBox="0 0 20 20"><circle cx="10" cy="10" r="9" fill="none" stroke="#33b8a4" stroke-width="1.6"/><path d="M5.5 10.5l3 3 6-6.5" fill="none" stroke="#abd037" stroke-width="2"/></svg>Low libido</li>
      <li><svg viewBox="0 0 20 20"><circle cx="10" cy="10" r="9" fill="none" stroke="#33b8a4" stroke-width="1.6"/><path d="M5.5 10.5l3 3 6-6.5" fill="none" stroke="#abd037" stroke-width="2"/></svg>Digestive health</li>
      <li><svg viewBox="0 0 20 20"><circle cx="10" cy="10" r="9" fill="none" stroke="#33b8a4" stroke-width="1.6"/><path d="M5.5 10.5l3 3 6-6.5" fill="none" stroke="#abd037" stroke-width="2"/></svg>Chronic fatigue syndrome</li>
      <li><svg viewBox="0 0 20 20"><circle cx="10" cy="10" r="9" fill="none" stroke="#33b8a4" stroke-width="1.6"/><path d="M5.5 10.5l3 3 6-6.5" fill="none" stroke="#abd037" stroke-width="2"/></svg>Perimenopause/menopause</li>
      <li><svg viewBox="0 0 20 20"><circle cx="10" cy="10" r="9" fill="none" stroke="#33b8a4" stroke-width="1.6"/><path d="M5.5 10.5l3 3 6-6.5" fill="none" stroke="#abd037" stroke-width="2"/></svg>Weight management</li>
      <li><svg viewBox="0 0 20 20"><circle cx="10" cy="10" r="9" fill="none" stroke="#33b8a4" stroke-width="1.6"/><path d="M5.5 10.5l3 3 6-6.5" fill="none" stroke="#abd037" stroke-width="2"/></svg>Type 2 diabetes, blood sugar dysregulation, high blood pressure, high cholesterol</li>
    </ul>
  </section>

  <div class="food-heart" role="img" aria-label="Heart arrangement of fresh vegetables, fruit and herbs"></div>

  <section class="contact">
    <p class="call">Call today on<br>085-4270-118</p>
    <p class="book">or email hello@brightorchardnutrition.ie<br>to book a consultation or for a free<br>no obligation 15 minute mini consultation.</p>
    <p class="clinic">Clinic consultations are held at the Riverside Wellness Rooms on Tuesdays and Thursdays. Home visits and evening appointments can also be arranged. Please book ahead to secure your place.</p>
  </section>
</main>
</body>
</html>
```